Help our pizza bases / flat breads fly off the shelves - You'll be seen in supermarkets New Zealand

Packaging design.
We have bought a product that is in desperate need of a complete re-brand. This includes a name, and a package design.
It is an rectangle shaped flat bread that can be used in many ways, and is presented 5 in a pack, in an unprinted flexible formed bottom, with a flat top film applied that is flat and ready to receive your design.
The product is mainly used as a pizza base bought by Mums to feed the family. It is also can be a pre dinner nibble like a pizza bread, and for quick and easy, you can cut one into 3 pieces, and toast in a pop-up toaster, before topping with whatever is in your fridge.
The current name is "Kelvo breads" which is just silly. The brand "Kelvo" needs to change to "Darby's Flat Breads" or whatever you might suggest. The product name might be "Gourmet Pizza Base" or "Gourmet Flat bread" as you like.
The look must get consumers to pick up the product and have a closer look. The nature of the graphics should emphasize the versatility and multi-usefulness, so the consumer can imagine what they will do with the product when they get it home. I feel that an informative pack will be better than a beautiful pack to get more sales. I have uploaded pictures showing the product currently in Supermarkets, and also a picture of the current product. Dimensions are 310 x 130mm.
You will need to leave room for: Barcode, Nutritional Panel, Cooking instructions, Storage instructions, Ingredients list and Company contact details - each one say 45 x 45mm or similar.
These details could go on the bottom of the low long side, as this is obscured while on shelf (see photo)
You will also highlight in your design, Preservative Free, 100% Natural, 5 Bases, Made with Olive oil, Hand made, and the variant (Roasted Garlic, or Original)
You will want to highlight the uses like: Pizza base, pizza bread, cut toast and top or similar.

```html
<!DOCTYPE html>
<html lang="en">
<head>
<meta charset="utf-8">
<title>Mr. Darby's Gourmet Flat Bread – Original</title>
<link rel="stylesheet" href="https://fonts.googleapis.com/css2?family=Yanone+Kaffeesatz:wght@500;700&family=Arvo:wght@400&family=Questrial&family=Montserrat:wght@800&display=swap">
<style>
  :root {
    --page: #ffffff;
    --wood-light: #f8dc86;
    --wood-mid: #f3cd6a;
    --wood-warm: #eebd58;
    --brown: #3d1a0c;
    --teal: #00a0b6;
    --teal-text: #1aa5bb;
    --white: #ffffff;
  }
  * { margin: 0; padding: 0; box-sizing: border-box; }
  html, body { width: 1200px; height: 1000px; overflow: hidden; background: var(--page); }
  .canvas { position: relative; width: 1200px; height: 1000px; }
  .label-shape { position: absolute; left: 0; top: 0; }
  .brand-name {
    position: absolute; left: 0; width: 1200px; top: 236px; text-align: center;
    font-family: "Yanone Kaffeesatz", sans-serif; font-weight: 700;
    font-size: 84px; line-height: 1; color: var(--brown); padding-left: 30px;
  }
  .range {
    position: absolute; left: 0; width: 1200px; top: 336px; text-align: center;
    font-family: "Yanone Kaffeesatz", sans-serif; font-weight: 700;
    font-size: 98px; line-height: 1; color: var(--brown); letter-spacing: 1px;
  }
  .product {
    position: absolute; left: 308px; top: 418px;
    font-family: "Yanone Kaffeesatz", sans-serif; font-weight: 700;
    font-size: 204px; line-height: 1; color: var(--brown); letter-spacing: 2px;
  }
  .variant {
    position: absolute; left: 307px; top: 588px;
    font-family: "Arvo", serif; font-size: 52px; line-height: 1;
    color: var(--teal-text); letter-spacing: 1px;
  }
  .uses-title {
    position: absolute; left: 221px; top: 681px;
    font-family: "Montserrat", sans-serif; font-weight: 800;
    font-size: 20px; letter-spacing: 2px; color: var(--white);
  }
  .uses-list {
    position: absolute; left: 220px; top: 706px;
    font-family: "Questrial", sans-serif; font-size: 37px;
    color: var(--white); word-spacing: 3px; white-space: nowrap;
  }
  .badge {
    position: absolute; left: 148px; top: 795px; width: 252px; height: 84px;
    border: 2px solid var(--white); border-radius: 10px; text-align: center;
    font-family: "Yanone Kaffeesatz", sans-serif; font-weight: 700; color: var(--white);
  }
  .badge-top { font-size: 25px; line-height: 1; margin-top: 6px; letter-spacing: 0.5px; }
  .badge-main { font-size: 46px; line-height: 1; letter-spacing: 0.5px; }
  .claim {
    position: absolute; left: 467px; top: 808px; width: 180px;
    font-family: "Questrial", sans-serif; font-size: 16.5px; line-height: 1.3;
    color: var(--white); letter-spacing: -0.3px;
  }
  .olive-mark { position: absolute; left: 645px; top: 800px; }
  .count {
    position: absolute; left: 913px; top: 826px;
    font-family: "Questrial", sans-serif; color: var(--white); line-height: 1; white-space: nowrap;
  }
  .count-num { font-size: 50px; }
  .count-unit { font-size: 29px; }
</style>
</head>
<body>
<main class="canvas">
  <svg class="label-shape" width="1200" height="1000" viewBox="0 0 1200 1000">
    <defs>
      <linearGradient id="wood" x1="0" y1="0" x2="1" y2="1">
        <stop offset="0" stop-color="var(--wood-light)"/>
        <stop offset="0.55" stop-color="var(--wood-mid)"/>
        <stop offset="1" stop-color="var(--wood-warm)"/>
      </linearGradient>
    </defs>
    <path class="board" role="img" aria-label="Light wooden board grain texture"
      d="M118 145 H296 C310 110 330 90 380 88 C440 86 470 72 540 72 C580 72 600 110 600 145 H1072 V660 H118 Z"
      fill="url(#wood)"/>
    <rect class="info-band" x="118" y="660" width="954" height="252" fill="var(--teal)"/>
    <line class="tear-line" x1="118" y1="768" x2="1072" y2="768"
      stroke="var(--white)" stroke-width="2" stroke-dasharray="9 7" opacity="0.85"/>
  </svg>

  <div class="brand-name">Mr. Darby's</div>
  <div class="range">-GOURMET-</div>
  <div class="product">Flat Bread</div>
  <div class="variant">ORIGINAL</div>

  <div class="uses-title">USE IT AS YOU LIKE!</div>
  <div class="uses-list">TOP it!&nbsp; – BAKE it!&nbsp; – FOLDit! –&nbsp; ROLL it!</div>

  <div class="badge">
    <div class="badge-top">PRESERVATIVE FREE</div>
    <div class="badge-main">100% NATURAL</div>
  </div>

  <p class="claim">Made handmade with 5 bases and natural olive oil.</p>
  <svg class="olive-mark" width="80" height="80" viewBox="0 0 80 80" role="img" aria-label="Olive branch sprig">
    <ellipse cx="40" cy="40" rx="34" ry="26" fill="var(--white)" opacity="0.35"/>
  </svg>

  <div class="count"><span class="count-num">5</span> <span class="count-unit">PCS.</span></div>
</main>
</body>
</html>
```